Product labels for new supplements business targeting high performing creative people

I need a label design for different supplements like Whey, BCAA, Melatonin etc. that I could customize for each use case separately.

The brand is called marrowly.club, and it would be the first design of the labels. We haven't sold any products yet, but the target audience is people with growth mindset, people who want to be as efficient as possible and are constantly looking to improve their lifestyle. As part of that, they are also working out, but don't know much about supplements yet. Mostly people between 20-34.

I don't have a too specific idea of the expected design, though it should be light, warm, smart and minimalist, maybe have some patterns. It should looks smart and clean (and expensive). Orange and golden might be the additional colors for white. I have attached the templates of some products that I plan to sell and also the logo of the brand.

Here's what I have used for inspiration:
Brands that I like and are somewhat similar in concept: https://www.vantipo.com/ (!!specially the way they
bring "how the product helps them" in focus, not "what the product is" & https://www.quib.care/ &
https://www.pelvoro.com/sport/ & https://en.sarfolia.fr/ &
https://craftmerge.com/profiles/noramaylinestudio/designs/418627

Here's how different products look like: https://vendrashop.com/catalog

Target Market(s)

target audience is people with growth mindset, people who want to be as efficient as possible and are constantly looking to improve their lifestyle. As part of that, they are also working out, but don't know much about supplements yet. Mostly people between 20-34.

Industry/Entity Type

Supplements

Font styles to use
Sans Serif

Colors
FFC000
F8CF3A
FAE287
FDF2CF
FEFAEE
F0912C
F2A743
F7CA91
FBE8D2
FDF5EE
EE7325
F08F49
F5BC92
FAE3D3
FDF4ED

Requirements
Must have
• Clean, smart and minimalist design that can be applied for different products in different sizes, like Whey protein, BCAA, vitamins etc. available here: https://vendrashop.com/catalog
Nice to have
• Patterns, expensive look
Should not have
• Doodles, too many colors

```html
<!DOCTYPE html>
<html lang="en">
<head>
<meta charset="utf-8">
<title>marrowly.club — Maca Root Powder label</title>
<link href="https://fonts.googleapis.com/css2?family=Roboto+Condensed:wght@400;700&family=Oswald:wght@600&family=Lexend:wght@500&display=swap" rel="stylesheet">
<style>
  :root {
    --canvas: #f4f4f4;
    --label-yellow: #f9dc3c;
    --band-orange: #f2a743;
    --diamond-gold: #f7c93a;
    --ink: #1b1b1b;
  }
  * { margin: 0; padding: 0; box-sizing: border-box; }
  html, body {
    width: 1200px; height: 1200px; overflow: hidden;
    background: var(--canvas);
  }
  .label {
    position: absolute; left: 150px; top: 96px;
    width: 900px; height: 1008px;
    background: var(--label-yellow);
    overflow: hidden;
    font-family: "Roboto Condensed", "Arial Narrow", sans-serif;
    color: var(--ink);
  }
  .label__pattern {
    position: absolute; inset: 0;
    background: linear-gradient(180deg, var(--label-yellow) 0%, #f8d83a 50%, var(--label-yellow) 100%);
  }
  .label__band {
    position: absolute; left: 0; width: 100%;
    background: var(--band-orange);
  }
  .label__band--top { top: 0; height: 88px; }
  .label__band--bottom { bottom: 0; height: 112px; }
  .label__diamond {
    position: absolute; left: 200px; top: 275px;
    width: 500px; height: 500px;
    background: var(--diamond-gold);
    border-radius: 60px;
    transform: rotate(45deg);
    opacity: .85;
  }
  .brand {
    position: absolute; top: 282px; left: 0; width: 100%;
    display: flex; justify-content: center; align-items: center; gap: 20px;
  }
  .brand__dot {
    width: 40px; height: 40px; border-radius: 50%;
    background: var(--ink);
  }
  .brand__name {
    font-family: "Lexend", sans-serif; font-weight: 500;
    font-size: 68px; letter-spacing: 1px; line-height: 1;
  }
  .product__name {
    position: absolute; top: 540px; left: 0; width: 100%;
    text-align: center;
    font-family: "Oswald", "Roboto Condensed", sans-serif; font-weight: 600;
    font-size: 100px; line-height: 1; letter-spacing: -1px;
    transform: scaleX(0.74);
  }
  .product__form {
    position: absolute; top: 652px; left: 0; width: 100%;
    text-align: center;
    font-size: 46px; font-weight: 400; letter-spacing: 1px; line-height: 1;
  }
  .product__benefits {
    position: absolute; top: 742px; left: 0; width: 100%;
    text-align: center;
    font-size: 30px; line-height: 40px; font-weight: 400;
  }
  .meta {
    position: absolute; top: 848px;
    font-size: 30px; font-weight: 400; line-height: 1;
  }
  .meta--type { left: 72px; letter-spacing: .5px; }
  .meta--weight { right: 90px; }
</style>
</head>
<body>
  <section class="label">
    <div class="label__pattern" role="img" aria-label="Fine scalloped wave pattern in warm yellow tones"></div>
    <div class="label__band label__band--top"></div>
    <div class="label__band label__band--bottom"></div>
    <div class="label__diamond"></div>

    <header class="brand">
      <span class="brand__dot"></span>
      <span class="brand__name">marrowly.club</span>
    </header>

    <h1 class="product__name">MACA ROOT</h1>
    <p class="product__form">POWDER</p>
    <p class="product__benefits">Helps reduce stress*<br>Increase enerygy and stamina</p>

    <p class="meta meta--type">DIETARY SUPPLEMENT</p>
    <p class="meta meta--weight">200g</p>
  </section>
</body>
</html>
```